Upmarket Bathroom and Kitchen ware supplier needs a classy business card design

We are a company based in Fiji, we sell plumbing ware (Kitchen and bathroom taps, Basins,showers, toilets etc) through up market show rooms to individuals and directly through Architects and designers of resorts and holiday houses for new builds and renovations. we are wanting to upgrade our over all look and brand. we are starting with a new logo but will be rebranding the whole business. This project is for a business card design for my management and tales team I would like it to be dark, classy and interesting

Target Market(s)

Resort directors and Management, High end holiday home owners

Contact Information for Business Card

Neil Dawson
Director
+64219473815

Colors

Designer to choose colors to be used in the design.

Requirements
Must have
• Must have an upmarket appearance I like darker charcoal shades but will be guided by the designers
• Please any catch phrases like "Crafting remarkable living rooms" this belongs tpo one of our suppliers so can not be used.
Nice to have
• Double sided, so front dedicated to logo provided and back info about the business and the person.

```html
<!DOCTYPE html>
<html lang="en">
<head>
<meta charset="utf-8">
<title>Coralview Interiors – Business Card</title>
<link href="https://fonts.googleapis.com/css2?family=Montserrat:wght@400;500&display=swap" rel="stylesheet">
<style>
  :root {
    --backdrop: #6f7074;
    --paper: #ffffff;
    --charcoal: #263746;
    --sand: #c2b59b;
    --ink: #263746;
    --text-light: #ffffff;
    --rule: #8c96a0;
  }
  html, body {
    margin: 0;
    padding: 0;
    width: 1200px;
    height: 1200px;
    overflow: hidden;
    background: var(--backdrop);
    font-family: "Montserrat", sans-serif;
  }
  .canvas {
    position: relative;
    width: 1200px;
    height: 1200px;
  }
  .card {
    position: absolute;
    left: 156px;
    width: 888px;
    background: var(--paper);
    overflow: hidden;
  }
  .card--front { top: 92px; height: 508px; }
  .card--back { top: 657px; height: 507px; }

  .sand-band {
    position: absolute;
    display: block;
  }
  .card--front .sand-band { left: 0; top: 417px; width: 888px; height: 91px; }
  .card--back .sand-band { left: 0; top: 442px; width: 888px; height: 65px; }
  .sand-band polygon { fill: var(--sand); }

  .brand-panel {
    position: absolute;
    left: 241px;
    top: 46px;
    width: 391px;
    height: 362px;
    background: var(--charcoal);
    color: var(--text-light);
    text-align: center;
  }
  .brand-name {
    position: absolute;
    left: 0;
    right: 0;
    top: 236px;
    margin: 0;
    font-weight: 400;
    line-height: 1;
    text-transform: uppercase;
  }
  .brand-name__main {
    display: block;
    font-size: 30px;
    letter-spacing: 0.3em;
    padding-left: 0.3em;
  }
  .brand-name__sub {
    display: block;
    width: 212px;
    margin: 12px auto 0;
    padding-top: 8px;
    border-top: 1px solid var(--rule);
    font-size: 13px;
    letter-spacing: 0.32em;
    padding-left: 0.32em;
    box-sizing: border-box;
  }
  .brand-tagline {
    position: absolute;
    left: 0;
    right: 0;
    top: 313px;
    margin: 0;
    font-size: 13px;
    font-weight: 400;
  }

  .person {
    position: absolute;
    left: 66px;
    top: 201px;
    color: var(--ink);
  }
  .person-name {
    margin: 0;
    font-size: 27px;
    font-weight: 500;
    line-height: 1.2;
  }
  .person-role {
    margin: 1px 0 0;
    font-size: 19px;
    font-weight: 400;
    letter-spacing: 0.05em;
  }
  .person-phone {
    margin: 3px 0 0;
    font-size: 20.5px;
    font-weight: 400;
    letter-spacing: 0.02em;
  }

  .about-panel {
    position: absolute;
    left: 315px;
    top: 0;
    width: 573px;
    height: 434px;
    background: var(--charcoal);
  }
  .about-text {
    position: absolute;
    left: 65px;
    top: 127px;
    margin: 0;
    width: 505px;
    color: var(--text-light);
    font-size: 20.5px;
    font-weight: 400;
    line-height: 25.5px;
    white-space: pre;
  }
</style>
</head>
<body>
<main class="canvas">

  <section class="card card--front" aria-label="Card front">
    <div class="brand-panel">
      <h1 class="brand-name">
        <span class="brand-name__main">Coralview</span>
        <span class="brand-name__sub">Interiors</span>
      </h1>
      <p class="brand-tagline">Refine your space...Refine your days.</p>
    </div>
    <svg class="sand-band" viewBox="0 0 888 91" preserveAspectRatio="none" aria-hidden="true">
      <polygon points="241,0 888,0 888,91 316,91"/>
    </svg>
  </section>

  <section class="card card--back" aria-label="Card back">
    <div class="person">
      <p class="person-name">Neil Dawson</p>
      <p class="person-role">Director</p>
      <p class="person-phone">+64219473815</p>
    </div>
    <div class="about-panel">
      <p class="about-text">We are a studio based in Suva,
we supply premium fixtures
 (Mixers and shower systems,
Vanities,baths, tiles etc)
through curated showrooms to
homeowners and directly through builders
and planners of hotels and island villas
for fresh projects and refurbishments.</p>
    </div>
    <svg class="sand-band" viewBox="0 0 888 65" preserveAspectRatio="none" aria-hidden="true">
      <polygon points="315,0 888,0 888,65 382,65"/>
    </svg>
  </section>

</main>
</body>
</html>
```